Invitation Design Project

50th Birthday Party for Tim. Big, loud party planned with loads of friends and family. at our home. Decorations will be coloured lanterns attached to the pergola and hired a band.

Details:

on 19th October, 2013
(other details when design chosen)
at: 7.00 pm
RSVP: 14th October, 2013

```html
<!DOCTYPE html>
<html lang="en">
<head>
<meta charset="utf-8">
<title>Tim's 50th Birthday Invitation</title>
<link rel="stylesheet" href="https://fonts.googleapis.com/css2?family=Euphoria+Script&family=Open+Sans:wght@400&display=swap">
<style>
  :root {
    --ink: #ffffff;
    --magenta: #b0236e;
    --violet: #5b2a78;
    --plum: #3a1530;
    --brick: #5a2a2a;
    --ember: #a8422a;
    --night: #000000;
    --band: rgba(20, 8, 14, 0.35);
  }
  html, body {
    margin: 0;
    padding: 0;
    overflow: hidden;
    background: var(--night);
  }
  .invitation {
    position: relative;
    width: 848px;
    height: 1200px;
    overflow: hidden;
    color: var(--ink);
    text-align: center;
    font-family: "Open Sans", Arial, sans-serif;
  }
  .venue-scene {
    position: absolute;
    inset: 0;
    background:
      radial-gradient(ellipse 300px 120px at 420px 340px, rgba(240, 140, 120, 0.45), transparent 70%),
      radial-gradient(ellipse 360px 260px at 700px 600px, rgba(150, 90, 170, 0.55), transparent 70%),
      radial-gradient(ellipse 260px 90px at 230px 1030px, rgba(220, 70, 40, 0.6), transparent 70%),
      linear-gradient(180deg, var(--magenta) 0%, var(--violet) 22%, var(--plum) 45%, var(--brick) 62%, var(--ember) 82%, var(--night) 88%, var(--night) 100%);
  }
  .verse-band {
    position: absolute;
    left: 0;
    top: 405px;
    width: 848px;
    height: 795px;
    background: var(--band);
  }
  .script {
    font-family: "Euphoria Script", "Brush Script MT", cursive;
    font-weight: 400;
    margin: 0;
    line-height: 1;
    position: absolute;
    left: 0;
    width: 848px;
  }
  .title-name { top: 40px; font-size: 80px; }
  .title-main { top: 152px; font-size: 118px; }
  .party-name { top: 752px; font-size: 68px; }
  .line {
    position: absolute;
    left: 0;
    width: 848px;
    margin: 0;
    line-height: 1;
  }
  .verse-caps { font-size: 28px; letter-spacing: 0.2px; }
  .verse { font-size: 25px; }
  .detail { font-size: 20px; }
</style>
</head>
<body>
  <main class="invitation">
    <div class="venue-scene" role="img" aria-label="Party venue photo: brick hall with pink and orange paper lanterns under a lit roof, crowd silhouettes with raised hands at the bottom"></div>
    <div class="verse-band"></div>

    <h1 class="script title-name">Tim's</h1>
    <p class="script title-main">50th Birthday</p>

    <p class="line verse-caps" style="top:470px">THE BIG 5-0 IS APPROACHING FAST</p>
    <p class="line verse-caps" style="top:506px">TIM IS OVER THE HILL AT LAST!</p>
    <p class="line verse" style="top:566px">Come celebrate and spread some cheer</p>
    <p class="line verse" style="top:600px">And let Gary know he's old this year!</p>

    <h2 class="script party-name">Tim's 50th Birthday Party</h2>
    <p class="line detail" style="top:816px">19th October, 2013,&nbsp; 7.00 pm</p>
    <p class="line detail" style="top:877px">Tim's Home</p>
    <p class="line detail" style="top:906px">RSVP&nbsp; 14th October, 2013</p>
  </main>
</body>
</html>
```